Energy Solution company Needs a PowerPoint Design

We need a PowerPoint design for new energy solution company based in Houston. major markets / clients in Africa called ''RV Mavrek Solutions'' . We provider variety of professional services, systems ,and project management solutions to Oil & Gas, Power , Telecommunication , ICT, Airlines & Transportation , Social & Public Sector and Utilities & Alternative Energy industries. We would like to see a simple PowerPoint designs but statement. The final design should communicate engineering Integrity, quality and safety. See attached file with template and company logo. please use logo color combination.

Target Market(s)

Oil & Gas, Power , Telecommunication , ICT, Airlines & Transportation , Social & Public Sector and Utilities & Alternative Energy industries.

Industry/Entity Type

It Company

Font styles to use
Other font styles liked:
• Century Gothic

Colors
ffc214
aaaaaa
0355a3

Requirements
Must have
• engineering details oriented simple looks. SEE ATTACHED PPT WITH COMPANY LOGO AND TEMPLATE. PLEASE ATTACHED LOGO COLOR COMBINATION.]
• We will like to see 5 text boxes with different images across the middle of the cover page, this images will be from below Industries:
• • Oil and Gas
• • Power
• • Information Technology
• • Manufacturing Industry
• • Higher Education Industry
• Please don't include the Industries name as list above, We just want the images.
Nice to have
• • Oil and Gas
• • Power

```html
<!DOCTYPE html>
<html lang="en">
<head>
<meta charset="utf-8">
<title>RV Mavrek Solutions – Presentation Template</title>
<link href="https://fonts.googleapis.com/css2?family=Questrial&family=Arimo:wght@400;700&display=swap" rel="stylesheet">
<style>
:root{
  --navy:#0c4868;
  --navy-faint:#2d6284;
  --gold:#f7b519;
  --blue:#1b5d9c;
  --rule:#1e4f7a;
  --ink:#333;
  --muted:#8a8a8a;
  --stage:#bcbcbc;
  --table-head:#86b6df;
  --table-cell:#bfdaf0;
  --table-cell-alt:#d3e6f6;
  --faint:#e3e8ee;
}
*{margin:0;padding:0;box-sizing:border-box}
html,body{width:1200px;height:640px;overflow:hidden;background:var(--stage)}
body{position:relative;font-family:"Arimo",Arial,sans-serif;color:var(--ink)}
.slide{position:absolute;width:374px;height:280px;background:#fff;overflow:hidden;box-shadow:6px 8px 10px rgba(0,0,0,.35)}
.slide--cover{left:14px;top:16px}
.slide--contents{left:409px;top:16px}
.slide--table{left:804px;top:16px}
.slide--charts{left:14px;top:323px}
.slide--closing{left:409px;top:323px;background:var(--navy)}
.abs{position:absolute}
.heading-font{font-family:"Questrial","Century Gothic",sans-serif;font-weight:400}

/* brand name */
.brand{font-family:"Questrial","Century Gothic",sans-serif;color:var(--navy);white-space:nowrap}

/* cover */
.cover__top-brand{left:0;width:100%;top:72px;text-align:center;font-size:21px}
.cover__gold{left:0;top:130px;width:100%;height:8px;background:var(--gold)}
.cover__panel{left:0;top:138px;width:100%;height:142px;background:var(--navy)}
.faint-disc{border-radius:50%;background:var(--navy-faint)}
.cover__disc{left:-30px;top:225px;width:95px;height:95px;opacity:.55}
.cover__title{left:70px;top:150px;font-size:21px;color:#fff}
.cover__lead{left:70px;top:184px;width:242px;font-size:7.6px;line-height:9.6px;color:#fff}
.contact-row{display:flex;gap:10px;font-size:6px;white-space:nowrap}
.cover__contacts{left:74px;top:262px;color:#fff}
.contact-row span{display:flex;align-items:center;gap:3px}
.contact-row svg{width:6px;height:6px}

/* header for inner slides */
.slide__title{left:32px;top:16px;font-size:12.5px;color:var(--navy)}
.slide__brand{right:22px;top:17px;font-size:9.5px}
.slide__rule{left:0;top:34px;width:100%;height:1.5px;background:var(--rule)}
.footer{left:0;bottom:0;width:374px;height:12px}
.footer__url{left:28px;bottom:3px;font-size:5px;font-weight:700;color:#fff}
.footer__num{right:38px;bottom:2px;font-size:6.5px;color:var(--navy)}

/* contents */
.contents__disc{left:10px;top:150px;width:110px;height:110px;background:var(--faint)}
.toc{left:27px;top:56px;width:327px;list-style:none}
.toc li{display:flex;align-items:flex-end;height:12px;font-size:5.6px;white-space:nowrap}
.toc__badge{width:8px;height:7px;background:var(--navy);color:#fff;font-size:5px;font-weight:700;text-align:center;line-height:7px;margin-right:4px}
.toc__main{color:var(--blue);font-weight:700}
.toc__sub{color:var(--muted);padding-left:31px}
.toc__leader{flex:1;border-bottom:.8px dotted #9aa;margin:0 6px 2px}
.toc__main .toc__leader{border-bottom:.8px solid var(--navy)}
.toc__page{width:8px;text-align:right;color:var(--navy);font-weight:700}

/* body text blocks */
.lead-bold{font-size:7.4px;line-height:9px;font-weight:700;color:var(--blue)}
.body-text{font-size:5.2px;line-height:9px;color:#444}
.table-slide__lead{left:24px;top:46px;width:330px}
.table-slide__body{left:24px;top:65px;width:330px}
.table-slide__after{left:24px;top:199px;width:330px}
.data-table{left:24px;top:112px;width:326px;border-collapse:collapse;font-size:5.6px}
.data-table th{background:var(--table-head);color:var(--navy);font-weight:400;height:10px;border:1px solid #fff;border-top:2px solid var(--rule)}
.data-table td{height:13.4px;background:var(--table-cell);border:1px solid #fff}
.data-table td:nth-child(even){background:var(--table-cell-alt)}

/* charts */
.chart-title{font-size:3.6px;line-height:4.4px;font-weight:700;text-align:center;color:#444;font-family:Georgia,serif}
.chart-block{left:22px;width:118px}
.charts__text{left:146px;top:43px;width:210px}
.charts__text .body-text{margin-top:3px}
.charts__text .body-text + .body-text{margin-top:8px}

/* closing */
.closing__disc{left:165px;top:40px;width:180px;height:180px;opacity:.5}
.closing__thanks{left:23px;top:186px;font-size:22px;color:#4f7c99}
.closing__gold{left:0;top:215px;width:100%;height:8px;background:var(--gold)}
.closing__white{left:0;top:223px;width:100%;height:57px;background:#fff}
.closing__brand{left:22px;top:240px;font-size:8px;line-height:10px}
.closing__contacts{left:79px;top:248px;color:var(--navy)}
.closing__contacts .contact-row + .contact-row{margin-top:5px}
</style>
</head>
<body>

<section class="slide slide--cover">
  <div class="abs brand cover__top-brand">RV Mavrek Solutions</div>
  <div class="abs cover__gold"></div>
  <div class="abs cover__panel"></div>
  <div class="abs faint-disc cover__disc"></div>
  <h1 class="abs heading-font cover__title">Headline of Presentation</h1>
  <p class="abs cover__lead">Lorem Ipsum is simply dummy text of the printing and typesetting industry. Lorem Ipsum has been the industry's standard dummy PageCraft Studio including versions of Lorem Ipsum.</p>
  <div class="abs contact-row cover__contacts">
    <span><svg viewBox="0 0 10 10"><path d="M2 1l2 2-1 1.5c.8 1.5 1.8 2.5 3.3 3.3L7.8 6.8l2 2L8.5 10C4.5 9.5.5 5.5 0 1.5z" fill="#fff"/></svg>00 005.214.7730</span>
    <span><svg viewBox="0 0 10 10"><rect x="0" y="2" width="10" height="6.5" fill="#fff"/><path d="M0 2l5 4 5-4" stroke="#0c4868" fill="none"/></svg>daniel.reyes@mailbox.com</span>
    <span><svg viewBox="0 0 10 10"><circle cx="5" cy="5" r="4.3" fill="none" stroke="#fff"/><ellipse cx="5" cy="5" rx="2" ry="4.3" fill="none" stroke="#fff"/><path d="M.7 5h8.6" stroke="#fff"/></svg>www.northlineworks.co.uk</span>
  </div>
</section>

<section class="slide slide--contents">
  <h2 class="abs heading-font slide__title">Content List</h2>
  <div class="abs brand slide__brand">RV Mavrek Solutions</div>
  <div class="abs slide__rule"></div>
  <div class="abs faint-disc contents__disc"></div>
  <ol class="abs toc">
    <li class="toc__main"><span class="toc__badge">A</span>Lorem Ipsum is simply dummy text<span class="toc__leader"></span><span class="toc__page">1</span></li>
    <li class="toc__sub">a) Of the printing and typesetting industry. Lorem Ipsum has been the try's<span class="toc__leader"></span><span class="toc__page">2</span></li>
    <li class="toc__sub">b) Standard dummy text ever since the 1500s, when an unknown printer<span class="toc__leader"></span><span class="toc__page">2</span></li>
    <li class="toc__main"><span class="toc__badge">A</span>Took a galley of type and scrambled it to<span class="toc__leader"></span><span class="toc__page">3</span></li>
    <li class="toc__sub">make a type specimen book. It has survived not only five centuries<span class="toc__leader"></span><span class="toc__page">4</span></li>
    <li class="toc__sub">leap into electronic typesetting, remaining<span class="toc__leader"></span><span class="toc__page">5</span></li>
    <li class="toc__sub">larised in the 1960s with the release of Lettrex sheets containing<span class="toc__leader"></span><span class="toc__page">6</span></li>
    <li class="toc__main"><span class="toc__badge">A</span>Lorem Ipsum passages, and more recently with desktop publishing software like<span class="toc__leader"></span><span class="toc__page">7</span></li>
    <li class="toc__main"><span class="toc__badge">A</span>PageCraft Studio including versions of Lorem Ipsum<span class="toc__leader"></span><span class="toc__page">7</span></li>
  </ol>
  <svg class="abs footer" viewBox="0 0 374 12" aria-hidden="true"><polygon points="0,0 302,0 298,12 0,12" fill="#0c4868"/><polygon points="307,0 374,0 374,12 303,12" fill="#f7b519"/></svg>
  <div class="abs footer__url">www.sitelinkhere.com</div>
  <div class="abs footer__num">2</div>
</section>

<section class="slide slide--table">
  <h2 class="abs heading-font slide__title">Heading Text place here</h2>
  <div class="abs brand slide__brand">RV Mavrek Solutions</div>
  <div class="abs slide__rule"></div>
  <p class="abs lead-bold table-slide__lead">Lorem Ipsum is simply dummy text of the printing and typesetting industry. Lorem Ipsum has been the industry's standard dummy text</p>
  <p class="abs body-text table-slide__body">Ever since the 1500s, when an unknown printer took a galley of type and scrambled it to make a type specimen book. It has survived not only five centuries, but also the leap into electronic typesetting, remaining essentially unchanged. It was popularised in the 1960s with the release of Lettrex sheets containing Lorem Ipsum passages, and more recently with desktop publishing software like PageCraft Studio including versions of Lorem Ipsum.</p>
  <table class="abs data-table">
    <colgroup><col style="width:82px"><col style="width:44px"><col style="width:86px"><col style="width:28px"><col></colgroup>
    <thead><tr><th>Contrary</th><th>Sale</th><th>Details</th><th>Rate</th><th>Comments</th></tr></thead>
    <tbody>
      <tr><td></td><td></td><td></td><td></td><td></td></tr>
      <tr><td></td><td></td><td></td><td></td><td></td></tr>
      <tr><td></td><td></td><td></td><td></td><td></td></tr>
      <tr><td></td><td></td><td></td><td></td><td></td></tr>
      <tr><td></td><td></td><td></td><td></td><td></td></tr>
    </tbody>
  </table>
  <p class="abs body-text table-slide__after">Contrary to popular belief, Lorem Ipsum is not simply random text. It has roots in a piece of classical Latin literature from 45 BC, making it over 2000 years old. Martin Halloway, a Latin professor at Brookfield College in Vermont, looked up one of the more obscure Latin words, consectetur, from a Lorem Ipsum passage, and going through the cites of the word in classical literature, discovered the undoubtable source. Lorem Ipsum comes from sections 1.10.32 and 1.10.33 of "de Ordine Formarum Veterum" (The Order of Old Forms) by Aurelian Dorso, written in 45 BC. This book is a treatise on the theory of ethics, very popular during the Renaissance. The first line of Lorem Ipsum, "Lorem ipsum dolor sit amet..", comes from a line in section 1.10.32.</p>
  <svg class="abs footer" viewBox="0 0 374 12" aria-hidden="true"><polygon points="0,0 302,0 298,12 0,12" fill="#0c4868"/><polygon points="307,0 374,0 374,12 303,12" fill="#f7b519"/></svg>
  <div class="abs footer__url">www.sitelinkhere.com</div>
  <div class="abs footer__num">3</div>
</section>

<section class="slide slide--charts">
  <h2 class="abs heading-font slide__title" style="left:26px">Heading Text place here</h2>
  <div class="abs brand slide__brand">RV Mavrek Solutions</div>
  <div class="abs slide__rule"></div>

  <div class="abs chart-block" style="top:51px">
    <p class="chart-title">Regional Output Share<br>For the year 2024</p>
    <svg width="118" height="70" viewBox="0 0 118 70" role="img" aria-label="Three-dimensional pie chart of regional output share">
      <g transform="translate(59 38) scale(2.2 1.1) rotate(-90)" opacity=".75">
        <circle r="10" fill="none" stroke="#6f6f8f" stroke-width="20"/>
      </g>
      <g transform="translate(59 32) scale(2.2 1.1) rotate(-90)" fill="none" stroke-width="20">
        <circle r="10" pathLength="100" stroke="#f7a88a" stroke-dasharray="18 82"/>
        <circle r="10" pathLength="100" stroke="#a6cc55" stroke-dasharray="16 84" stroke-dashoffset="-18"/>
        <circle r="10" pathLength="100" stroke="#f3d24a" stroke-dasharray="6 94" stroke-dashoffset="-34"/>
        <circle r="10" pathLength="100" stroke="#c2b0dc" stroke-dasharray="5 95" stroke-dashoffset="-40"/>
        <circle r="10" pathLength="100" stroke="#a9d6ee" stroke-dasharray="8 92" stroke-dashoffset="-45"/>
        <circle r="10" pathLength="100" stroke="#3f7fc0" stroke-dasharray="7 93" stroke-dashoffset="-53"/>
        <circle r="10" pathLength="100" stroke="#2aa6a6" stroke-dasharray="10 90" stroke-dashoffset="-60"/>
        <circle r="10" pathLength="100" stroke="#8e5aa8" stroke-dasharray="9 91" stroke-dashoffset="-70"/>
        <circle r="10" pathLength="100" stroke="#d9534f" stroke-dasharray="8 92" stroke-dashoffset="-79"/>
        <circle r="10" pathLength="100" stroke="#7fc6d6" stroke-dasharray="13 87" stroke-dashoffset="-87"/>
      </g>
    </svg>
  </div>

  <div class="abs chart-block" style="top:151px">
    <p class="chart-title">Regional Output Share<br>For the year 2025</p>
    <svg width="118" height="110" viewBox="0 0 118 110" role="img" aria-label="Doughnut chart of regional output share">
      <g transform="translate(59 55) scale(2.2) rotate(-90)" fill="none" stroke-width="10">
        <circle r="15" pathLength="100" stroke="#a6cc55" stroke-dasharray="16 84"/>
        <circle r="15" pathLength="100" stroke="#f3c53a" stroke-dasharray="7 93" stroke-dashoffset="-16"/>
        <circle r="15" pathLength="100" stroke="#3f7fc0" stroke-dasharray="6 94" stroke-dashoffset="-23"/>
        <circle r="15" pathLength="100" stroke="#b29bd6" stroke-dasharray="7 93" stroke-dashoffset="-29"/>
        <circle r="15" pathLength="100" stroke="#c0392b" stroke-dasharray="8 92" stroke-dashoffset="-36"/>
        <circle r="15" pathLength="100" stroke="#2aa6a6" stroke-dasharray="7 93" stroke-dashoffset="-44"/>
        <circle r="15" pathLength="100" stroke="#d4b23a" stroke-dasharray="5 95" stroke-dashoffset="-51"/>
        <circle r="15" pathLength="100" stroke="#5aa0d8" stroke-dasharray="6 94" stroke-dashoffset="-56"/>
        <circle r="15" pathLength="100" stroke="#4f8a3c" stroke-dasharray="8 92" stroke-dashoffset="-62"/>
        <circle r="15" pathLength="100" stroke="#8e4a9e" stroke-dasharray="7 93" stroke-dashoffset="-70"/>
        <circle r="15" pathLength="100" stroke="#1f9a8a" stroke-dasharray="7 93" stroke-dashoffset="-77"/>
        <circle r="15" pathLength="100" stroke="#f08a4b" stroke-dasharray="16 84" stroke-dashoffset="-84"/>
      </g>
    </svg>
  </div>

  <div class="abs charts__text">
    <p class="lead-bold">Lorem Ipsum is simply dummy text of the printing and typesetting industry.</p>
    <p class="body-text">Ever since the 1500s, when an unknown printer took a galley of type and scrambled it to make a type specimen book. It has survived not only five centuries, but also the leap into electronic typesetting, remaining essentially unchanged. It was popularised in the 1960s with the release of Lettrex sheets containing Lorem Ipsum passages, and more recently with desktop publishing software like PageCraft Studio including versions of Lorem Ipsum.</p>
    <p class="body-text">It is a long established fact that a reader will be distracted by the readable content of a page when looking at its layout. The point of using Lorem Ipsum is that it has a more-or-less normal distribution of letters, as opposed to using 'Content here, content here', making it look like readable English. Many desktop publishing packages and web page editors now use Lorem Ipsum as their default model text, and a search for 'lorem ipsum' will uncover many web sites still in their infancy. Various versions have evolved over the years, sometimes by accident, sometimes on purpose (injected humour and the like).</p>
    <p class="body-text">Contrary to popular belief, Lorem Ipsum is not simply random text. It has roots in a piece of classical Latin literature from 45 BC, making it over 2000 years old. Martin</p>
  </div>
  <svg class="abs footer" viewBox="0 0 374 12" aria-hidden="true"><polygon points="0,0 307,0 303,12 0,12" fill="#0c4868"/><polygon points="312,0 374,0 374,12 308,12" fill="#f7b519"/></svg>
  <div class="abs footer__url">www.sitelinkhere.com</div>
  <div class="abs footer__num">4</div>
</section>

<section class="slide slide--closing">
  <div class="abs faint-disc closing__disc"></div>
  <p class="abs heading-font closing__thanks">Thank You</p>
  <div class="abs closing__gold"></div>
  <div class="abs closing__white"></div>
  <div class="abs brand closing__brand">RV Mavrek<br>Solutions</div>
  <div class="abs closing__contacts">
    <div class="contact-row">
      <span><svg viewBox="0 0 10 10"><rect x="2.5" y="0" width="5" height="10" rx="1" fill="#0c4868"/></svg>00 005.214.7730</span>
      <span><svg viewBox="0 0 10 10"><rect x="2.5" y="0" width="5" height="10" rx="1" fill="#0c4868"/></svg>00 005.214.7731</span>
    </div>
    <div class="contact-row">
      <span><svg viewBox="0 0 10 10"><rect x="0" y="2" width="10" height="6.5" fill="#0c4868"/><path d="M0 2l5 4 5-4" stroke="#fff" fill="none"/></svg>daniel.reyes@mailbox.com</span>
      <span><svg viewBox="0 0 10 10"><circle cx="5" cy="5" r="4.3" fill="none" stroke="#0c4868"/><ellipse cx="5" cy="5" rx="2" ry="4.3" fill="none" stroke="#0c4868"/><path d="M.7 5h8.6" stroke="#0c4868"/></svg>www.northlineworks.co.uk</span>
    </div>
  </div>
</section>

</body>
</html>
```